Business Cards and Stationary for Dental Office
Brodley Dental
Use same font as used in my logo
R.T. Brodley
D.D.S, P.C.
418 West R. Parkway
Alder Falls, MO 64000
rtb@brodleydentalcare.test
www.brodleydentalcare.test
We are looking for clean, simple, professional designs. In addition to Business Card Design we would also like to see designs for letterhead and Envelope.

```html
<!DOCTYPE html>
<html lang="en">
<head>
<meta charset="utf-8">
<title>Brodley Dental — Stationery Set</title>
<link href="https://fonts.googleapis.com/css2?family=Raleway:wght@400;600;700&display=swap" rel="stylesheet">
<style>
:root{
  --bg:#e6e3df;
  --paper:#ffffff;
  --green:#1f8a3c;
  --green-dark:#0f6b2a;
  --green-light:#8fd18f;
  --grey:#8a8a8a;
  --grey-light:#d9d9d9;
  --ink:#3a3a3a;
}
*{margin:0;padding:0;box-sizing:border-box}
html,body{width:1200px;height:629px;overflow:hidden}
body{background:var(--bg);font-family:"Raleway",Arial,sans-serif;color:var(--ink);position:relative}
.sheet{position:absolute;background:var(--paper);box-shadow:0 2px 6px rgba(0,0,0,.18);overflow:hidden}
.wave{position:absolute;left:0;bottom:0;width:100%}
.brand{display:flex;align-items:center;gap:5px;position:absolute}
.brand-dot{border-radius:50%;background:var(--green)}
.brand-name{font-weight:700;color:var(--green);letter-spacing:.08em;text-transform:uppercase;white-space:nowrap}
.tiny{font-size:5px;line-height:1.5;color:var(--grey);position:absolute;white-space:nowrap}

/* envelope back */
.envelope-back{left:48px;top:396px;width:408px;height:126px}
.envelope-back .flap{position:absolute;left:0;top:0;width:100%;height:100%}
.envelope-back .seal{position:absolute;left:192px;top:50px;width:26px;height:26px;border-radius:50%;background:var(--green)}

/* envelope front */
.envelope-front{left:48px;top:505px;width:372px;height:88px}
.envelope-front .brand{left:12px;top:12px}
.envelope-front .web{right:12px;bottom:9px;color:#fff;font-size:5px}

/* business card */
.card-front{left:559px;top:34px;width:192px;height:110px}
.card-front .brand{left:10px;top:10px}
.card-back{left:763px;top:34px;width:192px;height:110px}
.appt-title{position:absolute;left:10px;top:10px;font-size:6px;color:var(--green);font-weight:600}
.appt-row{position:absolute;left:10px;display:flex;gap:4px;font-size:4.5px;color:var(--grey)}
.appt-row span.line{display:inline-block;width:34px;border-bottom:.5px solid var(--grey-light)}
.appt-box{display:inline-block;width:5px;height:5px;border:.5px solid var(--grey)}
.appt-note{position:absolute;left:10px;top:76px;font-size:4.5px;color:var(--green)}

/* letterhead & fax */
.letterhead{left:463px;top:173px;width:310px;height:410px}
.fax{left:828px;top:173px;width:312px;height:410px}
.letterhead .brand,.fax .brand{left:14px;top:14px}
.contact-col{left:180px;top:12px;border-left:.5px solid var(--grey-light);padding-left:5px}
.watermark-circle{position:absolute;left:105px;top:145px;width:100px;height:100px;border-radius:50%;background:#ececec}
.fax-title{position:absolute;left:14px;top:72px;font-size:20px;font-weight:400;color:var(--ink)}
.fax-rule{position:absolute;left:14px;right:14px;border-top:.6px solid var(--grey-light)}
.fax-fields{position:absolute;left:14px;top:110px;width:284px;display:grid;grid-template-columns:1fr 1fr;row-gap:11px;column-gap:14px}
.fax-field{font-size:5px;color:var(--grey);border-bottom:.5px solid var(--grey-light);padding-bottom:2px}
.fax-checks{position:absolute;left:14px;top:200px;display:flex;gap:18px;font-size:5px;color:var(--grey)}
.fax-checks span{display:flex;align-items:center;gap:3px}
.foot-addr{position:absolute;right:14px;bottom:7px;font-size:4.5px;color:#fff}
</style>
</head>
<body>

<!-- envelope back -->
<div class="sheet envelope-back">
  <svg class="flap" viewBox="0 0 408 126" preserveAspectRatio="none">
    <polyline points="0,0 204,70 408,0" fill="none" stroke="#cfcfcf" stroke-width="1"/>
    <polyline points="0,126 170,62" fill="none" stroke="#e3e3e3" stroke-width="1"/>
    <polyline points="408,126 238,62" fill="none" stroke="#e3e3e3" stroke-width="1"/>
  </svg>
  <div class="seal"></div>
</div>

<!-- envelope front -->
<div class="sheet envelope-front">
  <div class="brand"><span class="brand-dot" style="width:10px;height:10px"></span><span class="brand-name" style="font-size:7px">Brodley Dental</span></div>
  <div class="tiny" style="left:12px;top:28px">418 West R. Parkway, Alder Falls, MO 64000</div>
  <svg class="wave" viewBox="0 0 372 30" preserveAspectRatio="none" height="30">
    <path d="M0,18 C120,4 250,2 372,10 L372,30 L0,30Z" fill="var(--green-light)"/>
    <path d="M0,24 C140,12 260,12 372,16 L372,30 L0,30Z" fill="var(--green)"/>
  </svg>
  <div class="tiny web">www.brodleydentalcare.test</div>
</div>

<!-- business card front -->
<div class="sheet card-front">
  <div class="brand"><span class="brand-dot" style="width:9px;height:9px"></span><span class="brand-name" style="font-size:6px">Brodley Dental</span></div>
  <div class="tiny" style="left:10px;top:32px;color:var(--ink);font-size:5.5px;font-weight:600">R.T. Brodley, D.D.S, P.C.</div>
  <div class="tiny" style="left:10px;top:42px">Phone 555 014 2280<br>Fax 555 014 2281<br>rtb@brodleydentalcare.test<br>418 West R. Parkway<br>Alder Falls, MO 64000</div>
  <svg class="wave" viewBox="0 0 192 26" preserveAspectRatio="none" height="26">
    <path d="M0,14 C70,2 130,0 192,6 L192,26 L0,26Z" fill="var(--green-light)"/>
    <path d="M0,20 C80,10 140,10 192,12 L192,26 L0,26Z" fill="var(--green)"/>
  </svg>
</div>

<!-- business card back -->
<div class="sheet card-back">
  <div class="appt-title">Your next appointment is:</div>
  <div class="appt-row" style="top:26px">Mr./Ms. <span class="line" style="width:140px"></span></div>
  <div class="appt-row" style="top:38px">Date <span class="line"></span> Time <span class="line"></span></div>
  <div class="appt-row" style="top:50px">Next visit <span class="line" style="width:128px"></span></div>
  <div class="appt-row" style="top:62px;align-items:center">Mon <i class="appt-box"></i> Tue <i class="appt-box"></i> Wed <i class="appt-box"></i> Thu <i class="appt-box"></i> Fri <i class="appt-box"></i></div>
  <div class="appt-note">24 hours notice is kindly requested to cancel.</div>
  <svg class="wave" viewBox="0 0 192 18" preserveAspectRatio="none" height="18">
    <path d="M0,12 C70,4 130,2 192,6 L192,18 L0,18Z" fill="var(--green)"/>
  </svg>
</div>

<!-- letterhead -->
<div class="sheet letterhead">
  <div class="brand"><span class="brand-dot" style="width:14px;height:14px"></span><span class="brand-name" style="font-size:8px">Brodley Dental</span></div>
  <div class="tiny contact-col">Phone 555 014 2280<br>rtb@brodleydentalcare.test<br><br>418 West R. Parkway<br>Alder Falls, MO 64000</div>
  <div class="watermark-circle"></div>
  <svg class="wave" viewBox="0 0 310 44" preserveAspectRatio="none" height="44">
    <path d="M0,26 C110,4 210,2 310,12 L310,44 L0,44Z" fill="var(--green-light)"/>
    <path d="M0,32 C120,16 220,16 310,22 L310,44 L0,44Z" fill="var(--green)"/>
    <path d="M0,36 C130,22 230,22 310,26" fill="none" stroke="var(--grey-light)" stroke-width="1"/>
  </svg>
  <div class="tiny web" style="right:14px;bottom:8px;color:#fff">www.brodleydentalcare.test</div>
</div>

<!-- fax -->
<div class="sheet fax">
  <div class="brand"><span class="brand-dot" style="width:14px;height:14px"></span><span class="brand-name" style="font-size:8px">Brodley Dental</span></div>
  <div class="tiny contact-col" style="left:186px">Phone 555 014 2280<br>rtb@brodleydentalcare.test</div>
  <div class="fax-title">FAX</div>
  <div class="fax-rule" style="top:100px"></div>
  <div class="fax-fields">
    <div class="fax-field">To:</div><div class="fax-field">From:</div>
    <div class="fax-field">Fax:</div><div class="fax-field">Pages:</div>
    <div class="fax-field">Phone:</div><div class="fax-field">Date:</div>
    <div class="fax-field">Re:</div><div class="fax-field">CC:</div>
  </div>
  <div class="fax-checks">
    <span><i class="appt-box"></i>Urgent</span>
    <span><i class="appt-box"></i>For Review</span>
    <span><i class="appt-box"></i>Please Comment</span>
    <span><i class="appt-box"></i>Please Reply</span>
    <span><i class="appt-box"></i>Please Recycle</span>
  </div>
  <svg class="wave" viewBox="0 0 312 30" preserveAspectRatio="none" height="30">
    <path d="M0,14 C110,2 210,0 312,6 L312,30 L0,30Z" fill="var(--green-light)"/>
    <path d="M0,18 C120,8 220,8 312,12 L312,30 L0,30Z" fill="var(--green)"/>
  </svg>
  <div class="foot-addr">418 West R. Parkway, Alder Falls, MO 64000</div>
</div>

</body>
</html>
```